Christmas Flyer for Suburban London Cocktail Bar & Party Venue

We need a flyer with details of our Christmas Party drinks packages for party bookings. Tin and Thistle is a local cocktail bar with an emphasis on providing a modern hospitality environment with a sense of fun and whimsy. We pride ourselves on not being generic, providing a community atmosphere and don't take ourselves too seriously and our brand reflects that.

Christmas is one of the most popular times of year and we host parties for many people in our local area. The flyer is intended to summarise our promotional deals and will be distributed to local businesses as well as being available in the bar for customers.

An overview of our mood board that influences 'tone', as we await rebranding, can be seen at https://au.pinboardia.com/korvelmidge/commercial-bar-fit-out-inspiration/

Target Market(s)

21-35 Urban Professionals

Industry/Entity Type

Hospitality

Colors

Designer to choose colors to be used in the design.

Requirements
Must have
• The 4 offers contained in the copy text. Can be adjusted for legibility as long as the offers remain substantively the same.
• The logo of the bar. The standard logo is the gold version however that can be recoloured if appropriate.
• The Address Tin & Thistle - 27 Wrenmoor Rise - Balham, SW7 4KD - This need not be prominent.
Nice to have
• Our social media locations
• facebook /tinandthistlebar
• Instagram /tinandthistlebar
Should not have
• Should not contain photographs or exceptionally generic stock imagery.

```html
<!DOCTYPE html>
<html lang="en">
<head>
<meta charset="utf-8">
<title>Tin &amp; Thistle – Christmas Party Packages</title>
<link rel="stylesheet" href="https://fonts.googleapis.com/css2?family=Bebas+Neue&display=swap">
<style>
  :root {
    --stage: #e6e6e6;
    --paper: #ffffff;
    --berry: #8c1616;
    --berry-deep: #6f0f10;
    --pine: #207a66;
    --pine-deep: #17604f;
    --gold: #c9ab66;
    --ink-light: #ffffff;
    --font: "Bebas Neue", "Oswald", sans-serif;
  }
  * { box-sizing: border-box; margin: 0; padding: 0; }
  html, body { width: 1200px; height: 1000px; overflow: hidden; }
  body { background: var(--stage); font-family: var(--font); color: var(--ink-light); position: relative; }

  .flyer { position: absolute; }
  .flyer--red { left: 78px; top: 112px; width: 514px; height: 730px; background: var(--paper); padding: 13px 12px 14px 14px; }
  .flyer--green { left: 620px; top: 185px; width: 513px; height: 727px; }

  .flyer__face {
    position: relative; width: 100%; height: 100%; overflow: hidden;
    --logo-top: 28px; --banner-top: 230px; --grid-top: 300px; --grid-bottom: 627px;
    --rule-y: 154px; --rule-left: 0px; --rule-right: 45px; --footer-top: 664px;
  }
  .flyer--red .flyer__face { background: radial-gradient(ellipse at 50% 40%, var(--berry) 0%, var(--berry-deep) 100%); }
  .flyer--green .flyer__face {
    background: radial-gradient(ellipse at 50% 40%, var(--pine) 0%, var(--pine-deep) 100%);
    --logo-top: 70px; --banner-top: 243px; --grid-top: 310px; --grid-bottom: 645px;
    --rule-y: 155px; --rule-left: 70px; --rule-right: 60px; --footer-top: 660px;
  }

  .frame { position: absolute; inset: 0; width: 100%; height: 100%; }

  .brand {
    position: absolute; left: 0; right: 0; top: var(--logo-top);
    text-align: center; color: var(--gold); font-size: 74px; line-height: 0.95; letter-spacing: 2px;
  }

  .headline { position: absolute; left: 0; right: 0; top: var(--banner-top); height: 62px; }
  .headline__ribbon { position: absolute; left: 50%; top: 4px; width: 252px; height: 56px; margin-left: -126px; }
  .headline__text {
    position: absolute; left: 0; right: 0; top: 19px; text-align: center;
    font-size: 19px; letter-spacing: 0.5px; line-height: 1;
  }
  .mug {
    position: absolute; top: 0; width: 56px; height: 64px;
    background: var(--ink-light); border-radius: 4px 4px 6px 6px;
  }
  .mug--left { left: 56px; }
  .mug--right { right: 48px; }
  .flyer--green .mug--left { left: 72px; }
  .flyer--green .mug--right { right: 60px; }

  .packages {
    position: absolute; left: 0; right: 0; top: var(--grid-top); height: calc(var(--grid-bottom) - var(--grid-top));
    display: grid; grid-template-columns: 50% 50%; grid-template-rows: var(--rule-y) 1fr;
  }
  .packages::before {
    content: ""; position: absolute; left: 50%; top: 0; bottom: 0; width: 1.5px; background: var(--ink-light);
  }
  .packages::after {
    content: ""; position: absolute; top: var(--rule-y); left: var(--rule-left); right: var(--rule-right); height: 1.5px; background: var(--ink-light);
  }
  .package {
    display: flex; flex-direction: column; align-items: center; justify-content: center;
    text-align: center; padding: 0 6px; line-height: 1.05;
  }
  .package__name { color: var(--gold); font-size: 15px; letter-spacing: 0.3px; }
  .package__group { color: var(--gold); font-size: 13px; font-style: italic; margin-top: 2px; }
  .package__items { list-style: none; margin-top: 12px; font-size: 10.5px; line-height: 13px; }
  .package__group + .package__items { margin-top: 12px; }
  .package__name + .package__items { margin-top: 3px; }
  .package__note { font-size: 6px; line-height: 7px; font-style: italic; }
  .package__price { font-size: 26px; line-height: 1; margin-top: 10px; }
  .package__saving { font-size: 9.5px; margin-top: 3px; }

  .contact {
    position: absolute; left: 0; right: 0; top: var(--footer-top);
    display: flex; justify-content: space-between; padding: 0 48px 0 76px;
    font-size: 9.5px; line-height: 14px; letter-spacing: 0.3px;
  }
  .flyer--green .contact { padding: 0 68px 0 86px; }
  .contact__item { display: flex; align-items: center; gap: 5px; }
  .contact__pin { width: 10px; height: 13px; }
  .contact__square { width: 12px; height: 12px; background: var(--ink-light); border-radius: 2px; }
</style>
</head>
<body>

  <article class="flyer flyer--red">
    <div class="flyer__face">
      <h1 class="brand">TIN &amp;<br>THISTLE</h1>

      <header class="headline">
        <div class="mug mug--left" role="img" aria-label="Beer mug illustration"></div>
        <svg class="headline__ribbon" viewBox="0 0 252 56" aria-hidden="true">
          <path d="M2 4 H250 L232 28 L250 52 H2 L20 28 Z" fill="none" stroke="#fff" stroke-width="2.5"/>
          <rect x="22" y="10" width="208" height="36" fill="none" stroke="#fff" stroke-width="1.5"/>
        </svg>
        <h2 class="headline__text">CHRISTMAS PARTY PACKAGES</h2>
        <div class="mug mug--right" role="img" aria-label="Beer mug illustration"></div>
      </header>

      <section class="packages">
        <div class="package">
          <h3 class="package__name">SHARING COMBO</h3>
          <ul class="package__items"><li>3 OF OUR SHARING COCKTAILS</li><li>BOTTLE OF PROSECCO</li></ul>
          <p class="package__price">£85</p>
          <p class="package__saving">SAVE UP TO £35</p>
        </div>
        <div class="package">
          <h3 class="package__name">XMAS PACKAGE</h3>
          <p class="package__group">1 - 10 PEOPLE</p>
          <ul class="package__items"><li>10X COCKTAILS</li><li>10X BEERS</li><li>10X HOUSE SPIRIT + MIXER, GLASS OF WINE OR PROSECCO</li><li>BOTTLE OF PROSECCO</li></ul>
          <p class="package__price">£150</p>
          <p class="package__saving">SAVE UP TO £65</p>
        </div>
        <div class="package">
          <h3 class="package__name">XMAS PACKAGE 2</h3>
          <p class="package__group">15 PEOPLE</p>
          <ul class="package__items"><li>15X COCKTAILS</li><li>15X BEERS</li><li>15X HOUSE SPIRIT + MIXER, GLASS OF WINE OR PROSECCO</li><li>SHARING COCKTAIL</li></ul>
          <p class="package__price">£220</p>
          <p class="package__saving">SAVE UP TO £85</p>
        </div>
        <div class="package">
          <h3 class="package__name">XMAS PACKAGE 3</h3>
          <p class="package__group">20 PEOPLE</p>
          <ul class="package__items"><li>20X COCKTAILS</li><li>20X BEERS</li><li>20X HOUSE SPIRIT + MIXER, GLASS OF WINE OR PROSECCO</li><li>BOTTLE OF PROSECCO</li><li>TREASURE CHEST!</li><li class="package__note">12 PERSON SHARER VALUED AT £100</li></ul>
          <p class="package__price">£350</p>
          <p class="package__saving">SAVE UP TO £150</p>
        </div>
      </section>

      <footer class="contact">
        <span class="contact__item"><svg class="contact__pin" viewBox="0 0 10 13" aria-hidden="true"><path d="M5 0a5 5 0 0 1 5 5c0 3.5-5 8-5 8S0 8.5 0 5a5 5 0 0 1 5-5z" fill="#fff"/><circle cx="5" cy="5" r="2" fill="#7d1213"/></svg>27 WRENMOOR RISE - BALHAM, SW7 4KD</span>
        <span class="contact__item"><span class="contact__square"></span>TINANDTHISTLEBAR</span>
        <span class="contact__item"><span class="contact__square"></span>TINANDTHISTLEBAR</span>
      </footer>
    </div>
  </article>

  <article class="flyer flyer--green">
    <div class="flyer__face">
      <svg class="frame" viewBox="0 0 513 727" aria-hidden="true">
        <path d="M44 14 H469 A30 30 0 0 0 499 44 V683 A30 30 0 0 0 469 713 H44 A30 30 0 0 0 14 683 V44 A30 30 0 0 0 44 14 Z" fill="none" stroke="#fff" stroke-width="5"/>
        <path d="M46 25 H467 A21 21 0 0 0 488 46 V681 A21 21 0 0 0 467 702 H46 A21 21 0 0 0 25 681 V46 A21 21 0 0 0 46 25 Z" fill="none" stroke="#fff" stroke-width="2.5"/>
      </svg>

      <h1 class="brand">TIN &amp;<br>THISTLE</h1>

      <header class="headline">
        <div class="mug mug--left" role="img" aria-label="Beer mug illustration"></div>
        <svg class="headline__ribbon" viewBox="0 0 252 56" aria-hidden="true">
          <path d="M2 4 H250 L232 28 L250 52 H2 L20 28 Z" fill="none" stroke="#fff" stroke-width="2.5"/>
          <rect x="22" y="10" width="208" height="36" fill="none" stroke="#fff" stroke-width="1.5"/>
        </svg>
        <h2 class="headline__text">CHRISTMAS PARTY PACKAGES</h2>
        <div class="mug mug--right" role="img" aria-label="Beer mug illustration"></div>
      </header>

      <section class="packages">
        <div class="package">
          <h3 class="package__name">SHARING COMBO</h3>
          <ul class="package__items"><li>3 OF OUR SHARING COCKTAILS</li><li>BOTTLE OF PROSECCO</li></ul>
          <p class="package__price">£85</p>
          <p class="package__saving">SAVE UP TO £35</p>
        </div>
        <div class="package">
          <h3 class="package__name">XMAS PACKAGE</h3>
          <p class="package__group">1 - 10 PEOPLE</p>
          <ul class="package__items"><li>10X COCKTAILS</li><li>10X BEERS</li><li>10X HOUSE SPIRIT + MIXER, GLASS OF WINE OR PROSECCO</li><li>BOTTLE OF PROSECCO</li></ul>
          <p class="package__price">£150</p>
          <p class="package__saving">SAVE UP TO £65</p>
        </div>
        <div class="package">
          <h3 class="package__name">XMAS PACKAGE 2</h3>
          <p class="package__group">15 PEOPLE</p>
          <ul class="package__items"><li>15X COCKTAILS</li><li>15X BEERS</li><li>15X HOUSE SPIRIT + MIXER, GLASS OF WINE OR PROSECCO</li><li>SHARING COCKTAIL</li></ul>
          <p class="package__price">£220</p>
          <p class="package__saving">SAVE UP TO £85</p>
        </div>
        <div class="package">
          <h3 class="package__name">XMAS PACKAGE 3</h3>
          <p class="package__group">20 PEOPLE</p>
          <ul class="package__items"><li>20X COCKTAILS</li><li>20X BEERS</li><li>20X HOUSE SPIRIT + MIXER, GLASS OF WINE OR PROSECCO</li><li>BOTTLE OF PROSECCO</li><li>TREASURE CHEST!</li><li class="package__note">12 PERSON SHARER VALUED AT £100</li></ul>
          <p class="package__price">£350</p>
          <p class="package__saving">SAVE UP TO £150</p>
        </div>
      </section>

      <footer class="contact">
        <span class="contact__item"><svg class="contact__pin" viewBox="0 0 10 13" aria-hidden="true"><path d="M5 0a5 5 0 0 1 5 5c0 3.5-5 8-5 8S0 8.5 0 5a5 5 0 0 1 5-5z" fill="#fff"/><circle cx="5" cy="5" r="2" fill="#1c6d5b"/></svg>27 WRENMOOR RISE - BALHAM, SW7 4KD</span>
        <span class="contact__item"><span class="contact__square"></span>TINANDTHISTLEBAR</span>
        <span class="contact__item"><span class="contact__square"></span>TINANDTHISTLEBAR</span>
      </footer>
    </div>
  </article>

</body>
</html>
```